Book Cover for my Autobiography

I would like to see a CONCEPT of the Front Cover as per the following.
a) Take me out of the FILE NAMED=1-MAIN.jpg
b) I want my Wife "Watching over me" - behind me - in the SHADOWS. You can take her image for the concept from the FILE NAMED=2-Wife Watching over me.jpg.
c) This based on the old saying that "Behind every Good Man....is a Woman".  So that's what I want to convert because my wife has always been in the background, in the "Shadows" - always supporting and encouraging me in whatever I do.
d) This book is purely for my children, wife, siblings, relatives and Friends.
e) the Book Cover has to be designed FLAT & RECTANGULAR - like the sample leather cover.  i.e. NOT viewed from an Angle.
f) The Book Title is "Salt in the Orchard"
g) I have no pre-conceived ideas of design or colours or styling etc.  I want a PROFESSIONAL DESIGNER to come up with the best Overall Design that conveys the "Supportive Wife" always behind me and supporting me - While I am out front as the subject.
h) When the Design is accepted, I will provide the main photo of my wife without my son in front of her that I want to use - and one me without my wife's arms around me.  But if you can do that too (i.e. reconstruct my Wife's Burgundy top & and remove her arms from around me-then even better because I don't have to hire another graphic designer to do that for me).
My name is "Tomas Brenhoek" so the author of the autobiography needs to be SOMEWHERE.
h) And last, please just put some text - maybe 2 sentences for the summary of the story like many Autobiographies do. eg.
"My story of how ....Lorem ipsum dolor sit amet, consectetur adipiscing elit, sed do eiusmod tempor incididunt. Integer vitae justo eget magna fermentum iaculis eu non. Aliquam eleifend".

I forgot to mention that this Book Cover is actually going on an eBOOK - not a Printed Book.
It's just for Family and Friends.

```html
<!DOCTYPE html>
<html lang="en">
<head>
<meta charset="utf-8">
<title>Salt in the Orchard — Tomas Brenhoek</title>
<link rel="stylesheet" href="https://fonts.googleapis.com/css2?family=Great+Vibes&family=Noto+Sans:wght@400&display=swap">
<style>
  :root {
    --page-bg: #86bdf6;
    --cover-deep: #0f1d24;
    --cover-navy: #1c3346;
    --cover-moss: #2c3b24;
    --cover-olive: #4a5128;
    --wife-tone: #4a4a30;
    --author-hair: #2a2226;
    --author-skin: #a97f68;
    --author-blue: #2a2790;
    --ink-light: #ffffff;
    --ink-soft: #e9eef2;
  }
  html, body {
    margin: 0;
    padding: 0;
    width: 1200px;
    height: 1200px;
    overflow: hidden;
    background: var(--page-bg);
  }
  .canvas {
    position: relative;
    width: 1200px;
    height: 1200px;
  }
  .cover {
    position: absolute;
    left: 210px;
    top: 60px;
    width: 780px;
    height: 1080px;
    overflow: hidden;
    background:
      radial-gradient(ellipse at 30% 12%, rgba(74,81,40,0.55), transparent 45%),
      radial-gradient(ellipse at 85% 60%, rgba(60,70,40,0.45), transparent 50%),
      radial-gradient(ellipse at 60% 30%, rgba(40,70,100,0.55), transparent 55%),
      linear-gradient(160deg, var(--cover-navy) 0%, var(--cover-deep) 45%, var(--cover-moss) 100%);
    box-shadow: 0 8px 30px rgba(0,0,0,0.25);
  }
  .cover__wife-photo {
    position: absolute;
    left: 30px;
    top: 260px;
    width: 340px;
    height: 580px;
  }
  .cover__author-photo {
    position: absolute;
    left: 400px;
    top: 600px;
    width: 380px;
    height: 480px;
  }
  .cover__title {
    position: absolute;
    left: 0;
    top: 0;
    margin: 0;
    font-family: "Great Vibes", cursive;
    font-weight: 400;
    color: var(--ink-light);
    text-shadow: 2px 3px 4px rgba(0,0,0,0.85);
    line-height: 1;
  }
  .cover__title span {
    position: absolute;
    white-space: nowrap;
  }
  .cover__title .title-line--first { left: 420px; top: 150px; font-size: 130px; }
  .cover__title .title-line--second { left: 285px; top: 250px; font-size: 92px; }
  .cover__title .title-line--third { left: 400px; top: 320px; font-size: 120px; }
  .cover__author {
    position: absolute;
    left: 430px;
    top: 478px;
    margin: 0;
    font-family: "Noto Sans", sans-serif;
    font-weight: 400;
    font-size: 30px;
    letter-spacing: 0.5px;
    color: var(--ink-light);
    text-shadow: 1px 2px 3px rgba(0,0,0,0.8);
  }
  .cover__summary {
    position: absolute;
    left: 38px;
    top: 880px;
    width: 340px;
    margin: 0;
    font-family: "Noto Sans", sans-serif;
    font-size: 15px;
    line-height: 1.6;
    color: var(--ink-soft);
    text-shadow: 1px 1px 2px rgba(0,0,0,0.8);
  }
</style>
</head>
<body>
<main class="canvas">
  <section class="cover" aria-label="Book cover: Salt in the Orchard by Tomas Brenhoek">
    <svg class="cover__wife-photo" width="340" height="580" viewBox="0 0 340 580" role="img" aria-label="Faint portrait of the author's wife, smiling, fading into the shadows behind him">
      <defs>
        <radialGradient id="wife-glow" cx="0.5" cy="0.4" r="0.5">
          <stop offset="0" stop-color="var(--wife-tone)" stop-opacity="0.6"/>
          <stop offset="0.55" stop-color="var(--wife-tone)" stop-opacity="0.25"/>
          <stop offset="1" stop-color="var(--wife-tone)" stop-opacity="0"/>
        </radialGradient>
      </defs>
      <rect width="340" height="580" fill="url(#wife-glow)"/>
    </svg>

    <svg class="cover__author-photo" width="380" height="480" viewBox="0 0 380 480" role="img" aria-label="Photograph of the author, smiling, in a blue sweater over a red checked collar">
      <defs>
        <filter id="soft-edge" x="-30%" y="-30%" width="160%" height="160%">
          <feGaussianBlur stdDeviation="22"/>
        </filter>
        <radialGradient id="author-upper" cx="0.5" cy="0.45" r="0.5">
          <stop offset="0" stop-color="var(--author-skin)" stop-opacity="0.85"/>
          <stop offset="0.7" stop-color="var(--author-hair)" stop-opacity="0.7"/>
          <stop offset="1" stop-color="var(--author-hair)" stop-opacity="0"/>
        </radialGradient>
      </defs>
      <g filter="url(#soft-edge)">
        <ellipse cx="210" cy="170" rx="120" ry="150" fill="url(#author-upper)"/>
        <ellipse cx="230" cy="450" rx="200" ry="150" fill="var(--author-blue)" opacity="0.9"/>
      </g>
    </svg>

    <h1 class="cover__title">
      <span class="title-line--first">Salt</span>
      <span class="title-line--second">in the</span>
      <span class="title-line--third">Orchard</span>
    </h1>

    <p class="cover__author">Tomas Brenhoek</p>

    <p class="cover__summary">"My story of how ....Lorem ipsum dolor sit amet, consectetur adipiscing elit, sed do eiusmod tempor incididunt. Integer vitae justo eget magna fermentum iaculis eu non. Aliquam eleifend".</p>
  </section>
</main>
</body>
</html>
```